I need a bag for flour with windows from the front ill attach some sample title is BRAMBLE CRUST PREMIX FLOUR
with color changing on the side stand up pouch I want to be able to put stickers ford different type of flour

Target Market(s)

retail store

Industry/Entity Type

flour retails

Font styles to use
Serif

Colors
0094D4
00A9DD
6FCCEA
C7EBF8
E9F6FB
00AB8E
00BBA5
67D7C9
C6EFE9
E9F9F6

Requirements
Must have
• creative
Nice to have
• I need a place so I can place the stickers of the flour
Should not have
• simple

```html
<!DOCTYPE html>
<html lang="en">
<head>
<meta charset="utf-8">
<title>Bramble Crust Premix Flour – Stand-up Pouch</title>
<link rel="stylesheet" href="https://fonts.googleapis.com/css2?family=Playfair+Display:wght@400;700;900&display=swap">
<style>
  :root {
    --page-bg: #e4e6e7;
    --mint-pale: #e9f9f6;
    --mint-light: #c6efe9;
    --mint: #67d7c9;
    --teal: #00bba5;
    --teal-deep: #00ab8e;
    --band-green: #1c8a6c;
    --forest: #163a34;
    --forest-dark: #10262a;
    --ink: #1f2a2a;
    --window-white: #f4f6f6;
    --sketch-tone: #a9d9cf;
  }
  * { margin: 0; padding: 0; box-sizing: border-box; }
  html, body {
    width: 983px;
    height: 1200px;
    overflow: hidden;
    background: var(--page-bg);
  }
  .canvas {
    position: relative;
    width: 983px;
    height: 1200px;
  }
  .pouch {
    position: absolute;
    left: 146px;
    top: 60px;
    width: 690px;
    height: 1080px;
    overflow: hidden;
    border-radius: 6px 6px 10px 10px;
    background: linear-gradient(100deg, var(--mint-light) 0%, #a9e6dc 45%, var(--mint-light) 75%, #b3e9df 100%);
  }
  .pouch svg.pouch-art {
    position: absolute;
    inset: 0;
  }
  .zip-seal {
    position: absolute;
    left: 0;
    top: 104px;
    width: 100%;
    height: 3px;
    background: rgba(255,255,255,0.45);
  }
  .landscape-left,
  .landscape-right,
  .wheat-stalks {
    position: absolute;
    border-radius: 40% 50% 20% 30%;
  }
  .landscape-left {
    left: 30px; top: 60px; width: 180px; height: 130px;
    background: radial-gradient(ellipse at 50% 60%, rgba(120,190,175,0.35), rgba(120,190,175,0) 70%);
  }
  .landscape-right {
    left: 505px; top: 50px; width: 180px; height: 290px;
    background: radial-gradient(ellipse at 50% 55%, rgba(120,190,175,0.35), rgba(120,190,175,0) 70%);
  }
  .wheat-stalks {
    left: 20px; top: 300px; width: 260px; height: 230px;
    background: radial-gradient(ellipse at 45% 40%, rgba(70,110,100,0.35), rgba(70,110,100,0) 70%);
  }
  .brand-panel {
    position: absolute;
    left: 216px;
    top: 0;
    width: 285px;
    height: 378px;
    background: linear-gradient(180deg, #2fb79c 0%, #44bfa7 60%, #3ab49c 100%);
    display: flex;
    flex-direction: column;
    align-items: center;
    padding-top: 160px;
  }
  .brand-name {
    font-family: "Playfair Display", serif;
    font-weight: 400;
    color: var(--ink);
    font-size: 38px;
    letter-spacing: 5px;
    line-height: 1.2;
    text-align: center;
  }
  .sticker-label {
    position: absolute;
    left: 189px;
    top: 418px;
    width: 316px;
    text-align: center;
    font-family: "Playfair Display", serif;
    font-weight: 700;
    font-size: 25px;
    line-height: 1.25;
    color: var(--ink);
  }
  .quality-seal {
    position: absolute;
    left: 545px;
    top: 515px;
    width: 118px;
    height: 118px;
    border-radius: 50%;
    background: var(--forest);
    border: 5px solid var(--window-white);
    box-shadow: 0 0 0 3px var(--forest);
    transform: rotate(-15deg);
  }
  .title-band {
    position: absolute;
    left: 0;
    top: 740px;
    width: 100%;
    height: 156px;
    background: linear-gradient(180deg, #1f9274 0%, var(--band-green) 100%);
    text-align: center;
  }
  .title-brand {
    display: block;
    font-family: "Playfair Display", serif;
    font-weight: 700;
    font-size: 70px;
    line-height: 1;
    color: #ffffff;
    margin-top: 14px;
    letter-spacing: -1px;
  }
  .title-product {
    display: block;
    font-family: "Playfair Display", serif;
    font-weight: 900;
    font-size: 64px;
    line-height: 1;
    color: var(--forest);
    margin-top: 6px;
    letter-spacing: 0;
  }
  .base-band {
    position: absolute;
    left: 0;
    top: 896px;
    width: 100%;
    height: 184px;
    background: linear-gradient(180deg, var(--forest) 0%, var(--forest-dark) 100%);
  }
  .weight-tag {
    position: absolute;
    left: 266px;
    top: 1000px;
    width: 224px;
    height: 80px;
    background: var(--window-white);
    border-radius: 16px 16px 0 0;
    display: flex;
    align-items: center;
    justify-content: center;
    font-family: "Playfair Display", serif;
    font-weight: 900;
    font-size: 46px;
    color: var(--ink);
  }
</style>
</head>
<body>
<main class="canvas">
  <section class="pouch" aria-label="Bramble Crust premix flour stand-up pouch, front">
    <div class="zip-seal"></div>
    <div class="landscape-left" role="img" aria-label="Faint sketch of trees and fields"></div>
    <div class="landscape-right" role="img" aria-label="Faint sketch of a farmhouse and rolling hills"></div>
    <div class="brand-panel">
      <p class="brand-name">BRAMBLE<br>CRUST</p>
    </div>
    <div class="wheat-stalks" role="img" aria-label="Line drawing of wheat ears"></div>

    <svg class="pouch-art" width="690" height="1080" viewBox="0 0 690 1080" aria-hidden="true">
      <path class="window-outline" d="M505,478 C625,498 690,630 690,748" fill="none" stroke="#1d2b2b" stroke-width="5"/>
      <path class="window-outline" d="M150,548 C105,600 88,680 88,748" fill="none" stroke="#1d2b2b" stroke-width="5"/>
      <path class="sticker-window" d="M189,409 Q189,389 209,389 L485,389 Q505,389 505,409 L505,498 C618,516 676,640 676,748 L80,748 C80,645 128,565 189,540 Z" fill="#f4f6f6"/>
    </svg>

    <p class="sticker-label">WHOLE WHEAT<br>FLOUR</p>
    <div class="quality-seal" role="img" aria-label="Quality seal"></div>

    <div class="title-band">
      <span class="title-brand">BRAMBLE CRUST</span>
      <span class="title-product">PREMIX FLOUR</span>
    </div>
    <div class="base-band"></div>
    <div class="weight-tag">500g</div>
  </section>
</main>
</body>
</html>
```